Stationary and Business Card for Law Firm
Modern, Professional & Sophisticated Law Firm Card
Stationary and Business Card for Law Firm - Law
Creative Brief
Professional
Owen Barker
Partner
482 North Mill Avenue Pelham, Illinois 62904
obarker@barkerwynn.example
www.barkerwynn.example
These cards will be used by three attorneys, so I would like to be able to change the names out. Alternatively, if you could insert the names when providing source files, it would be appreciated. Names are: Owen B. Barker Rosalind P. Barker Natalie K. Wynn Emails are: obarker@barkerwynn.example rbarker@barkerwynn.example nwynn@barkerwynn.example
pbruner27 pbruner27
While I like the look many of the envelopes, the return address must be in the upper right hand corner to meet US Postal regulations. Firm Name/Logo Address City, State Zip (additional design info if you like) I have had similar envelopes on a different project with the Logo address on the lower part of the envelope---the post office refused to accept them.

```html
<!DOCTYPE html>
<html lang="en">
<head>
<meta charset="utf-8">
<title>Barker &amp; Wynn – Business Card</title>
<link rel="stylesheet" href="https://fonts.googleapis.com/css2?family=Cinzel:wght@400&family=Work+Sans:wght@300;400&display=swap">
<style>
  :root {
    --backdrop: #262626;
    --card: #0d0d0d;
    --gloss: #3b3b3b;
    --gloss-soft: #2f2f2f;
    --text-light: #c4c4c4;
    --text-muted: #8a8a8a;
    --divider: #5a5a5a;
  }
  * { margin: 0; padding: 0; box-sizing: border-box; }
  html, body {
    width: 1200px;
    height: 901px;
    overflow: hidden;
    background: var(--backdrop);
  }
  .stage {
    position: relative;
    width: 1200px;
    height: 901px;
  }
  .card {
    position: absolute;
    left: 250px;
    width: 700px;
    height: 400px;
    background: var(--card);
    border-radius: 3px;
    box-shadow: 0 10px 30px rgba(0,0,0,0.45);
  }
  .card--front { top: 34px; }
  .card--back { top: 467px; }

  /* Front */
  .firm-mark {
    position: absolute;
    left: 0; right: 0;
    top: 150px;
    text-align: center;
  }
  .firm-name {
    font-family: "Cinzel", serif;
    font-size: 52px;
    font-weight: 400;
    letter-spacing: 1px;
    color: var(--gloss);
    line-height: 1;
  }
  .firm-tagline {
    display: block;
    margin-top: 6px;
    padding-left: 170px;
    font-family: "Cinzel", serif;
    font-size: 15px;
    letter-spacing: 2px;
    color: var(--gloss);
  }

  /* Back */
  .attorney {
    position: absolute;
    left: 60px;
    top: 150px;
    width: 230px;
    text-align: right;
  }
  .attorney-name {
    font-family: "Cinzel", serif;
    font-size: 30px;
    color: var(--gloss);
    line-height: 1;
    letter-spacing: 0.5px;
  }
  .attorney-title {
    margin-top: 6px;
    font-family: "Work Sans", sans-serif;
    font-size: 14px;
    font-weight: 300;
    color: var(--gloss);
    padding-right: 8px;
  }
  .divider {
    position: absolute;
    left: 318px;
    top: 140px;
    width: 1px;
    height: 100px;
    background: var(--divider);
  }
  .contact-list {
    position: absolute;
    left: 338px;
    top: 140px;
    list-style: none;
    font-family: "Work Sans", sans-serif;
    font-size: 16px;
    font-weight: 400;
    color: var(--text-light);
  }
  .contact-item {
    display: flex;
    align-items: center;
    height: 25px;
  }
  .contact-icon {
    width: 12px;
    height: 12px;
    margin-right: 10px;
    fill: var(--text-light);
  }
  .address {
    position: absolute;
    left: 0; right: 0;
    top: 318px;
    text-align: center;
    font-family: "Work Sans", sans-serif;
    font-size: 16px;
    font-weight: 300;
    color: var(--text-muted);
  }
</style>
</head>
<body>
<main class="stage">
  <section class="card card--front">
    <div class="firm-mark">
      <div class="firm-name">BARKER &amp; WYNN</div>
      <span class="firm-tagline">ATTORNEYS AT LAW</span>
    </div>
  </section>

  <section class="card card--back">
    <div class="attorney">
      <div class="attorney-name">OWEN BARKER</div>
      <div class="attorney-title">Partner</div>
    </div>
    <div class="divider"></div>
    <ul class="contact-list">
      <li class="contact-item">
        <svg class="contact-icon" viewBox="0 0 12 12" aria-hidden="true"><path d="M2.5 0.8 4.3 3 3.4 4.2c.7 1.6 2 2.9 3.6 3.6L8.2 6.9l2.2 1.8-.9 2.3C5 10.7 1.3 7 1 2.5z"/></svg>
        217.555.0142
      </li>
      <li class="contact-item">
        <svg class="contact-icon" viewBox="0 0 12 12" aria-hidden="true"><rect x="3" y="1" width="6" height="3"/><rect x="1" y="4.5" width="10" height="4.5" rx="1"/><rect x="3" y="8" width="6" height="3"/></svg>
        217.555.0186
      </li>
      <li class="contact-item">
        <svg class="contact-icon" viewBox="0 0 12 12" aria-hidden="true"><path d="M1 2.5h10v7H1z M1.5 3 6 6.5 10.5 3" fill="none" stroke="#c4c4c4" stroke-width="1"/></svg>
        obarker@barkerwynn.example
      </li>
      <li class="contact-item">
        <svg class="contact-icon" viewBox="0 0 12 12" aria-hidden="true"><circle cx="6" cy="6" r="5"/></svg>
        www.barkerwynn.example
      </li>
    </ul>
    <p class="address">482 North Mill Avenue Pelham, Illinois 62904</p>
  </section>
</main>
</body>
</html>
```